Accounting firm needs a postcard design

We need a postcard design for our accounting office for a advertising campaign mailing we do yearly from a mail list we create. We are a full-service accounting office that has been in business for 35 years. I have attached our logo in different formats along with a document with a description of the services we provide. I have also attached my business card and the business card of our CPA. The business cards will have contact information for the postcard design. The contact email that will need to be on the postcard is contact@marlowtaxpartners.com.

```html
<!DOCTYPE html>
<html lang="en">
<head>
<meta charset="utf-8">
<title>Marlow Tax Partners – Postcard</title>
<link rel="stylesheet" href="https://fonts.googleapis.com/css2?family=Montserrat:wght@400;500;600;700;800&family=Playfair+Display:wght@700&display=swap">
<style>
  :root{
    --navy:#1f2d6b;
    --blue:#1e5aa8;
    --green:#5db033;
    --green-dark:#3a8f2a;
    --ink:#2a2f3a;
    --paper:#ffffff;
    --paper-soft:#eef1f4;
    --backdrop:#dfe2e6;
    --line:#c9ced6;
  }
  *{margin:0;padding:0;box-sizing:border-box}
  html,body{width:1200px;height:900px;overflow:hidden}
  body{background:var(--backdrop);font-family:"Montserrat",sans-serif;color:var(--ink);position:relative}
  .postcard{position:absolute;left:285px;width:630px;height:420px;background:var(--paper);overflow:hidden;box-shadow:0 2px 10px rgba(0,0,0,.12)}
  .postcard--front{top:20px;background:linear-gradient(90deg,var(--paper) 0%,var(--paper) 40%,var(--paper-soft) 100%)}
  .postcard--back{top:460px}
  .postcard svg.art{position:absolute;inset:0;width:630px;height:420px}

  .brand{position:absolute;display:flex;align-items:center;gap:8px}
  .brand__dot{width:14px;height:14px;border-radius:50%;background:var(--green)}
  .brand__name{font-family:"Montserrat",sans-serif;font-weight:800;color:var(--navy);letter-spacing:.06em;text-transform:uppercase;white-space:nowrap}
  .brand__tagline{position:absolute;font-size:8px;color:var(--ink);font-weight:500;white-space:nowrap}

  /* front */
  .front__brand{left:32px;top:64px}
  .front__brand .brand__name{font-size:17px}
  .front__tagline{left:54px;top:88px;font-size:8.5px}
  .front__person{position:absolute;left:32px;top:128px;font-weight:700;font-size:13.5px;line-height:1.3;color:#111}
  .front__headline{position:absolute;left:32px;top:172px;width:272px;font-family:"Playfair Display",serif;font-weight:700;font-size:22px;line-height:1.18;color:var(--blue)}
  .contact{position:absolute;left:32px;top:285px}
  .contact__title{font-weight:800;font-size:15px;color:var(--navy);margin-bottom:6px}
  .contact__row{display:flex;align-items:center;gap:8px;font-size:13px;font-weight:500;color:#111;line-height:22px;white-space:nowrap}
  .icon{width:14px;height:14px;flex:none}

  /* back */
  .services{position:absolute;left:26px;top:26px;width:318px}
  .service{margin-bottom:9px}
  .service__title{font-weight:800;font-size:11px;color:var(--blue);letter-spacing:.02em}
  .service__text{font-size:8.4px;line-height:1.35;color:#222;text-align:justify}
  .back__band{position:absolute;left:18px;top:356px;display:grid;grid-template-columns:auto auto;column-gap:22px;row-gap:4px;font-weight:600;color:#fff}
  .back__band .contact__row{color:#fff;font-size:11px;line-height:18px}
  .back__band .contact__row--wide{grid-column:1 / 3}
  .stamp{position:absolute;right:30px;top:22px;width:82px;height:64px;border:1px solid var(--line)}
  .back__brand{right:30px;top:112px}
  .back__brand .brand__name{font-size:11px}
  .back__tagline{right:30px;top:130px;font-size:5.5px}
  .address-line{position:absolute;left:450px;width:150px;height:1px;background:var(--line)}
</style>
</head>
<body>

<section class="postcard postcard--front" aria-label="Postcard front">
  <svg class="art" viewBox="0 0 630 420">
    <defs>
      <radialGradient id="photoTone" cx="50%" cy="55%" r="60%">
        <stop offset="0%" stop-color="#c9a57a"/>
        <stop offset="45%" stop-color="#e6d6c6"/>
        <stop offset="100%" stop-color="#b9c7b0"/>
      </radialGradient>
      <linearGradient id="leafA" x1="0" y1="0" x2="0" y2="1">
        <stop offset="0%" stop-color="#7cc242"/>
        <stop offset="100%" stop-color="#3a8f2a"/>
      </linearGradient>
    </defs>
    <polygon points="382,42 568,42 618,140 618,262 560,352 392,352 332,254 332,140"
             fill="var(--navy)" stroke="var(--navy)" stroke-width="34" stroke-linejoin="round"/>
    <circle cx="475" cy="196" r="128" fill="url(#photoTone)" role="img"
            aria-label="Photo of two hands sheltering a young plant growing from a pile of coins"/>
    <path d="M490,420 C560,360 620,300 605,190 C645,250 660,330 620,420 Z" fill="url(#leafA)"/>
    <path d="M440,380 C490,340 595,300 580,180 C610,230 620,300 560,345 C525,370 480,380 440,380 Z" fill="var(--green)"/>
  </svg>

  <div class="brand front__brand">
    <span class="brand__dot"></span>
    <span class="brand__name">Marlow Tax Partners</span>
  </div>
  <p class="brand__tagline front__tagline">Tax Preparation | Bookkeeping | Payroll | Entity Formation</p>

  <p class="front__person">Lena Marlow, CPA<br>Professional Corporation</p>
  <h1 class="front__headline">Individualized Business and Personal Accounting services you can trust.</h1>

  <div class="contact">
    <h2 class="contact__title">CONTACT US</h2>
    <p class="contact__row"><svg class="icon" viewBox="0 0 14 14"><circle cx="7" cy="7" r="7" fill="var(--green)"/><path d="M7 3.2a2.3 2.3 0 0 0-2.3 2.3c0 1.7 2.3 4.3 2.3 4.3s2.3-2.6 2.3-4.3A2.3 2.3 0 0 0 7 3.2z" fill="#fff"/></svg>418 Alder Street, Bayview, CA</p>
    <p class="contact__row"><svg class="icon" viewBox="0 0 14 14"><circle cx="7" cy="7" r="7" fill="var(--green)"/><path d="M4.5 3.5l1.4-.3.8 1.8-.9.7a5 5 0 0 0 2.5 2.5l.7-.9 1.8.8-.3 1.4c-3.4.2-6.2-2.6-6-6z" fill="#fff"/></svg>555-014-2290</p>
    <p class="contact__row"><svg class="icon" viewBox="0 0 14 14"><circle cx="7" cy="7" r="7" fill="var(--green)"/><rect x="3.5" y="4.5" width="7" height="5" fill="#fff"/><path d="M3.5 4.5L7 7.3l3.5-2.8" stroke="var(--green)" stroke-width=".8" fill="none"/></svg>contact@marlowtaxpartners.com</p>
    <p class="contact__row"><svg class="icon" viewBox="0 0 14 14"><circle cx="7" cy="7" r="7" fill="var(--green)"/><circle cx="7" cy="7" r="3.6" fill="none" stroke="#fff" stroke-width=".9"/><path d="M3.4 7h7.2M7 3.4c-1.6 2-1.6 5.2 0 7.2M7 3.4c1.6 2 1.6 5.2 0 7.2" stroke="#fff" stroke-width=".7" fill="none"/></svg>www.marlowtaxpartners.com</p>
  </div>
</section>

<section class="postcard postcard--back" aria-label="Postcard back">
  <svg class="art" viewBox="0 0 630 420">
    <path d="M325,0 C385,20 405,70 395,140 C387,200 397,260 445,300" fill="none" stroke="var(--blue)" stroke-width="3"/>
    <path d="M380,40 C420,100 405,190 420,250 C435,310 485,330 545,340" fill="none" stroke="var(--green)" stroke-width="4"/>
    <path d="M0,348 L440,348 L410,420 L0,420 Z" fill="var(--navy)"/>
  </svg>

  <div class="services">
    <article class="service">
      <h3 class="service__title">TAX PREPARATION</h3>
      <p class="service__text">With over 35 years of experience filing tax returns, we are experts in tax preparation. Including Personal Returns, Corporations, LLC's, Partnerships &amp; State Franchise Tax Returns.</p>
    </article>
    <article class="service">
      <h3 class="service__title">BOOKKEEPING</h3>
      <p class="service__text">Let us take over the day-to-day bookkeeping so you can get back to running your business. We offer assistance with LedgerPro setup and provide ongoing bookkeeping services. Including frequent journal entries, accounts payables and receivables, sales tax reporting &amp; payments, account reconciliation &amp; more.</p>
    </article>
    <article class="service">
      <h3 class="service__title">FINANCIAL REPORTING</h3>
      <p class="service__text">We'll provide easy to understand financial reports that allow you &amp; your team to manage cash flow, create budgets &amp; make forecasting decisions. Depending on your needs, we can provide monthly, quarterly or yearly financial statements.</p>
    </article>
    <article class="service">
      <h3 class="service__title">PAYROLL PROCESSING</h3>
      <p class="service__text">Whether you have 5 employees or 100+, payroll can be an overwhelming and time consuming task. We offer full-service payroll processing. Including employee onboarding, printed or direct deposit checks, quarterly payroll report filing, yearly W-2/W-3 and 1099 printing and filing, and more.</p>
    </article>
  </div>

  <div class="back__band">
    <p class="contact__row"><svg class="icon" viewBox="0 0 14 14"><circle cx="7" cy="7" r="6.3" fill="none" stroke="var(--green)" stroke-width="1.2"/><path d="M4.5 3.5l1.4-.3.8 1.8-.9.7a5 5 0 0 0 2.5 2.5l.7-.9 1.8.8-.3 1.4c-3.4.2-6.2-2.6-6-6z" fill="var(--green)"/></svg>555-014-2290</p>
    <p class="contact__row"><svg class="icon" viewBox="0 0 14 14"><circle cx="7" cy="7" r="6.3" fill="none" stroke="var(--green)" stroke-width="1.2"/><circle cx="7" cy="7" r="3.4" fill="none" stroke="var(--green)" stroke-width=".9"/><path d="M3.6 7h6.8M7 3.6c-1.5 2-1.5 4.8 0 6.8M7 3.6c1.5 2 1.5 4.8 0 6.8" stroke="var(--green)" stroke-width=".7" fill="none"/></svg>www.marlowtaxpartners.com</p>
    <p class="contact__row contact__row--wide"><svg class="icon" viewBox="0 0 14 14"><circle cx="7" cy="7" r="6.3" fill="none" stroke="var(--green)" stroke-width="1.2"/><rect x="3.8" y="4.8" width="6.4" height="4.4" fill="var(--green)"/><path d="M3.8 4.8L7 7.2l3.2-2.4" stroke="var(--navy)" stroke-width=".7" fill="none"/></svg>contact@marlowtaxpartners.com</p>
  </div>

  <div class="stamp" aria-label="Stamp area"></div>

  <div class="brand back__brand">
    <span class="brand__dot" style="width:10px;height:10px"></span>
    <span class="brand__name">Marlow Tax Partners</span>
  </div>
  <p class="brand__tagline back__tagline">Tax Preparation | Bookkeeping | Payroll | Entity Formation</p>

  <span class="address-line" style="top:180px"></span>
  <span class="address-line" style="top:228px"></span>
  <span class="address-line" style="top:276px"></span>
</section>

</body>
</html>
```